VORLEX/M&P - brochure vol III

We have 2 property companies;
VORLEX – Development Consultants - http://vorlex.co.uk/
Marsh & Pennard Commercial – Commercial Property Agents - http://marshandpennard.com/
We have 2 VORLEX brochures and 1 Marsh & Pennard brochure, with almost the same content.
We need someone to design a 3rd brochure. The content will be a combination of the content of in our previous brochures. We can provide all images and text. Once the brochure is designed, we will need 2 versions – almost identical content but 2 different front covers (one for each company).
We have many reference examples of brochure designs that we love.
Any questions please let me know!
Thank you,
Greta

```html
<!DOCTYPE html>
<html lang="en">
<head>
<meta charset="utf-8">
<title>VORLEX – Brochure Volume III</title>
<link href="https://fonts.googleapis.com/css2?family=Montserrat:wght@400;500;600;700&display=swap" rel="stylesheet">
<style>
:root{
  --stage:#333333;
  --cover:#262626;
  --amber:#fbb034;
  --sun:#f8d511;
  --title-amber:#f5b51c;
  --ink:#2e2e2e;
  --muted:#6b6b6b;
  --paper:#ffffff;
  --paper-soft:#f1f1f1;
  --slate:#555555;
  --map-dark:#3e3c40;
  --map-light:#d9d9d9;
}
*{margin:0;padding:0;box-sizing:border-box}
html,body{width:1200px;height:1181px;overflow:hidden;background:var(--stage)}
body{font-family:'Montserrat',Arial,sans-serif;color:var(--ink);position:relative}
.page{position:absolute;width:353px;height:249px;background:var(--paper);overflow:hidden}
.ph{position:absolute}
.c1{left:33px}.c2{left:417px}.c3{left:801px}
.r1{top:38px}.r2{top:326px}.r3{top:610px}.r4{top:895px}

/* cover */
.cover{background:var(--cover)}
.cover-frame{position:absolute;left:101px;top:71px;width:150px;height:95px;border:1px solid var(--amber);text-align:center;color:var(--amber)}
.cover-name{font-size:33px;font-weight:600;letter-spacing:1px;margin-top:12px;line-height:1}
.cover-tag{font-size:8px;font-weight:600;line-height:1.5;margin-top:8px}
.cover-vol{position:absolute;left:0;width:100%;top:174px;text-align:center;color:var(--amber);font-size:9.5px;font-weight:600}

/* maps */
.focus-label{position:absolute;left:15px;top:122px;transform:rotate(-90deg);transform-origin:left top;color:var(--amber);font-size:13px;font-weight:700;letter-spacing:.5px;white-space:nowrap}
.map-dark{background:linear-gradient(160deg,#4a474c,var(--map-dark) 60%,#343236)}
.map-light{background:linear-gradient(160deg,#e6e6e6,var(--map-light) 40%,#6a686c 65%,#5a585c)}
.about-title{position:absolute;top:164px;width:100%;text-align:center;color:var(--amber);font-size:15px;font-weight:700}
.about-body{position:absolute;left:32px;right:32px;top:185px;font-size:4.6px;line-height:1.45;color:var(--muted);text-align:justify}
.about-body p+p{margin-top:3px}

/* project sheets */
.bar{position:absolute;top:0;height:100%;width:15px;background:var(--amber)}
.bar.right{right:0;width:10px}
.title{font-size:9.5px;font-weight:700;line-height:1.1;color:var(--ink)}
.kind{font-size:5.2px;font-weight:600;color:var(--amber);margin-top:3px;text-transform:uppercase}
.lead{font-size:4.6px;line-height:1.45;color:var(--muted);margin-top:8px}
.facts{list-style:none;margin-top:7px;font-size:4.8px;line-height:2.1;color:var(--muted)}
.facts b{color:var(--ink);font-weight:600}
.copy{position:absolute}
.boxed{border:1px solid var(--amber);border-right:none;padding:12px 8px 8px 12px}
.on-amber .title{color:#fff}
.on-amber .kind{color:var(--ink)}
.on-amber .lead{color:#fff}
.on-amber .facts{color:#fff}
.on-amber .facts b{color:#fff;font-weight:700}
.hex{background:var(--paper-soft)}

.panel-slate{position:absolute;left:209px;top:35px;width:144px;height:67px;background:var(--slate);padding:9px 12px;color:#fff}
.panel-slate .title{color:var(--sun);font-size:9.5px}
.sub{font-size:5.4px;font-weight:700;margin-top:4px;text-transform:uppercase}
.mini{font-size:4.8px;line-height:2;margin-top:4px}
.mini b{font-weight:600}
.panel-amber{position:absolute;left:0;top:170px;width:175px;height:79px;background:var(--amber);padding:9px 15px;color:#fff}
.panel-amber .mini b{color:#fff;font-weight:700}

/* back */
.back{background:var(--paper-soft)}
.back-band{position:absolute;left:0;top:86px;width:100%;height:74px;background:var(--sun);text-align:center;padding-top:10px}
.icons{display:flex;justify-content:center;gap:3px}
.icons span{width:8px;height:8px;border-radius:50%;background:#fff;display:block}
.contact{font-size:5.8px;line-height:1.5;margin-top:4px;color:var(--ink)}
</style>
</head>
<body>

<section class="page cover c1 r1">
  <div class="cover-frame">
    <div class="cover-name">VORLEX</div>
    <div class="cover-tag">LONDON'S DEVELOPMENT<br>CONSULTANT</div>
  </div>
  <div class="cover-vol">VOLUME III</div>
</section>

<section class="page c2 r1 hex">
  <div class="focus-label">FOCUS AREAS</div>
  <div class="ph map-dark" style="left:31px;top:14px;width:307px;height:220px" role="img" aria-label="Dark map of London boroughs with the Thames traced in amber"></div>
</section>

<section class="page c3 r1 hex">
  <div class="ph map-light" style="left:16px;top:14px;width:320px;height:142px" role="img" aria-label="Map of south-east London boroughs with the Thames traced in amber"></div>
  <div class="ph" style="left:16px;top:156px;width:320px;height:80px;background:#fff"></div>
  <h2 class="about-title">ABOUT US</h2>
  <div class="about-body">
    <p>VORLEX Property is a leading London based development consultancy specialising in the acquisition and disposal of brownfield sites with potential for residential development.</p>
    <p>Our expertise is in identifying opportunities where developers can add value through planning permission or strategic asset management. Our considerable knowledge of the development market and creative approach to delivering maximum value has enabled us to become one of the most active development consultancies in South/East London and Kent.</p>
  </div>
</section>

<section class="page c1 r2">
  <div class="bar"></div>
  <div class="copy" style="left:26px;top:15px;width:140px">
    <div class="title">67 TALLOW STREET,<br>LONDON SE1</div>
    <div class="kind">Landmark development</div>
    <p class="lead" style="margin-top:22px">Acquisition of an existing office building with the benefit of full planning permission for the development of a 16 storey mixed use scheme.</p>
    <ul class="facts">
      <li><b>Scheme</b> – 9 x Luxury apartments; 16 storeys</li>
      <li><b>Borough</b> – Southwark</li>
      <li><b>Existing use</b> – Office</li>
      <li><b>Vendor/Selling agent</b> – Fenwick Realty</li>
      <li><b>Purchaser</b> – Private Client</li>
      <li><b>Project value</b> – £20,000,000</li>
    </ul>
  </div>
  <div class="ph" style="left:167px;top:15px;width:171px;height:220px;background:linear-gradient(180deg,#dfe7ee,#a88c7c 55%,#8a7e78)" role="img" aria-label="Street photo of a brick office tower"></div>
  <div class="ph" style="left:16px;top:199px;width:150px;height:36px;background:linear-gradient(90deg,#b7a99a,#cfd3d6)" role="img" aria-label="Row of small photos of the building"></div>
</section>

<section class="page c2 r2">
  <div class="ph" style="left:14px;top:14px;width:324px;height:91px;background:linear-gradient(135deg,#8d8d8d,#b4b4b4 50%,#7a7a7a)" role="img" aria-label="Aerial photo of the site outlined in red"></div>
  <div class="copy" style="left:20px;top:115px;width:180px">
    <div class="title">1-9 HARLOW CROSS STREET,<br>LONDON E1</div>
    <div class="kind">Residential development site</div>
    <p class="lead" style="margin-top:2px">Identified and delivered development opportunity with planning permission for a mixed use scheme comprising 78 apartments in the City Fringe.</p>
    <ul class="facts" style="line-height:2">
      <li><b>Scheme</b> – 78 x Residential apartments</li>
      <li><b>Borough</b> – Tower Hamlets</li>
      <li><b>Existing use</b> – Car repairs centre</li>
      <li><b>Vendor/Selling agent</b> – Colbrook Agents</li>
      <li><b>Purchaser</b> – Redgate Homes Trust</li>
      <li><b>Project value</b> – £30,000,000</li>
    </ul>
  </div>
  <div class="ph" style="left:208px;top:109px;width:130px;height:73px;background:linear-gradient(160deg,#9aa58a,#7a7f7c)" role="img" aria-label="Photo of rooftop and parking"></div>
  <div class="ph" style="left:208px;top:186px;width:130px;height:48px;background:linear-gradient(160deg,#a9b6bf,#9a7a70)" role="img" aria-label="Photo of nearby buildings"></div>
</section>

<section class="page c3 r2">
  <div class="bar"></div>
  <div class="copy boxed" style="left:26px;top:46px;width:141px;height:152px">
    <div class="title">LINDEN STREET,<br>MAIDSTONE ME16</div>
    <div class="kind">Residential development site</div>
    <p class="lead" style="margin-top:6px">Delivered consented development site with planning permission for 22 dwellings to housing association, off market.</p>
    <ul class="facts" style="line-height:2.2">
      <li><b>Scheme</b> – 22 x Social housing units</li>
      <li><b>Borough</b> – Maidstone</li>
      <li><b>Existing use</b> – Business Centre</li>
      <li><b>Vendor/Selling agent</b> – Private individual</li>
      <li><b>Purchaser</b> – Alder Housing Association</li>
      <li><b>Project value</b> – £5,000,000</li>
    </ul>
  </div>
  <div class="ph" style="left:167px;top:14px;width:171px;height:141px;background:linear-gradient(180deg,#c9d8e2,#a6775f 50%,#8da07a)" role="img" aria-label="Illustration of new brick houses"></div>
  <div class="ph" style="left:167px;top:162px;width:171px;height:74px;background:linear-gradient(135deg,#f0f0f0,#cdd3c6)" role="img" aria-label="Site layout plan"></div>
</section>

<section class="page c1 r3 hex">
  <div class="ph" style="left:14px;top:15px;width:173px;height:108px;background:linear-gradient(180deg,#e2e6e8,#b68a6a 55%,#8e7a70)" role="img" aria-label="Visual of brick apartment block"></div>
  <div class="ph" style="left:14px;top:126px;width:173px;height:108px;background:linear-gradient(180deg,#d9e0e5,#c0a47e 55%,#7f7a76)" role="img" aria-label="Street view of the scheme"></div>
  <div class="ph" style="left:187px;top:0;width:156px;height:249px;background:#fff"></div>
  <div class="copy boxed" style="left:187px;top:47px;width:151px;height:152px;border-left:none;border-right:1px solid var(--amber);padding-left:12px">
    <div class="title">ASHFORD ROAD,<br>LONDON SE5</div>
    <div class="kind">Petrol filling station</div>
    <p class="lead" style="margin-top:6px">Acquisition of small petrol station portfolio from Petrova Fuels including site in Camberwell with planning permission for the development of 9 apartments and a retail space let to Greengrove Stores.</p>
    <ul class="facts" style="line-height:2">
      <li><b>Scheme</b> – 9 x Private flats</li>
      <li><b>Borough</b> – Southwark</li>
      <li><b>Existing use</b> – Petrol Station</li>
      <li><b>Vendor/Selling agent</b> - Petrova Fuels</li>
      <li><b>Purchaser</b> – Private client</li>
      <li><b>Project value</b> – £7,000,000</li>
    </ul>
  </div>
  <div class="bar right"></div>
</section>

<section class="page c2 r3 on-amber">
  <div class="ph" style="left:0;top:0;width:164px;height:249px;background:var(--amber)"></div>
  <div class="copy boxed" style="left:26px;top:46px;width:138px;height:154px;border-color:#fff">
    <div class="title">BRAYTON ROAD,<br>LONDON SW19</div>
    <div class="kind">Petrol filling station</div>
    <p class="lead" style="margin-top:6px">Part of Petrova Portfolio the site was acquired off market with a pending planning application for a mixed use development comprising 9 flats and retail space let to Greengrove Stores.</p>
    <ul class="facts" style="line-height:2.1">
      <li><b>Scheme</b> – 9 x Private flats</li>
      <li><b>Borough</b> – Merton</li>
      <li><b>Existing use</b> – Petrol Filling Station</li>
      <li><b>Vendor/Selling agent</b> – Petrova Fuels</li>
      <li><b>Purchaser</b> – Private client</li>
      <li><b>Project value</b> – £7,500,000</li>
    </ul>
  </div>
  <div class="ph" style="left:164px;top:18px;width:189px;height:212px;background:linear-gradient(180deg,#dfe8ee,#b9a48c 45%,#6c6560)" role="img" aria-label="Visual of new corner building with shopfront"></div>
</section>

<section class="page c3 r3">
  <div class="ph" style="left:0;top:0;width:353px;height:249px;background:linear-gradient(180deg,#e6ecf0,#cdd6da 45%,#9fa3a5 70%,#c9c9c9)" role="img" aria-label="Street photo of a low commercial building"></div>
  <div class="panel-slate">
    <div class="title">CALDER HILL SW2</div>
    <div class="sub">Acquisition</div>
    <div class="mini"><b>Borough</b> - Lambeth<br><b>Project Value</b> - £7,000,000</div>
  </div>
</section>

<section class="page c1 r4">
  <div class="ph" style="left:0;top:0;width:175px;height:249px;background:linear-gradient(180deg,#e4e6e8,#9a8f86 50%,#6f6c6a)" role="img" aria-label="Photo of a residential tower under construction"></div>
  <div class="copy" style="left:189px;top:15px;width:160px">
    <div class="title" style="color:var(--title-amber)">ELMSTEAD ROAD<br>SE22</div>
    <div class="sub" style="color:var(--ink)">Acquisition</div>
    <div class="mini" style="line-height:1.9"><b>Scheme</b> - 9 Units<br><b>Borough</b> - Southwark<br><b>Project value</b> - £6,000,000</div>
  </div>
  <div class="ph" style="left:175px;top:86px;width:178px;height:163px;background:linear-gradient(180deg,#dfe7ee,#c9cccd 50%,#8d8f90)" role="img" aria-label="Photo of building wrapped in scaffolding"></div>
  <div class="panel-amber">
    <div class="title" style="color:#fff">WEXFORD ROAD KT1</div>
    <div class="sub" style="color:var(--ink)">Acquisition</div>
    <div class="mini" style="line-height:2.2"><b>Scheme</b> - 35 Units + Commercial<br><b>Borough</b> - Kingston<br><b>Project value</b> - £15,000,000</div>
  </div>
</section>

<section class="page back c2 r4">
  <div class="back-band">
    <div class="icons"><span></span><span></span><span></span><span></span></div>
    <p class="contact">42 LARKFIELD ROW, LONDON SE1 4QT<br>0207 555 0186<br>INFO@VORLEX.CO.UK<br>WWW.VORLEX.CO.UK</p>
  </div>
</section>

</body>
</html>
```